Utility Contractor looking for a new website

Water and wastewater utility contractor looking to create a new website that highlights our various services. We are looking for modern web presence that can be updated with current projects and new services as we grow. We have an existing logo that we would like to incorporate into the overall design of the site
Updates

Hi, Thank you for all the design submissions. I have had some time to review and have eliminated the ones I feel are not what I am looking for. Based on the designs that remain, I am looking for a clean (not to many bold colours), modern look that is not to busy (long scrolling page), Thanks, Dean

Target Market(s)

project managers, strata boards, owners, people who make decisions as to who operates their water/wastewater system

Industry/Entity Type

Utility

Font styles to use
Sans Serif

Requirements
Must have
• A min page that describes the company and what we do, A page for each of our services that outlines the service and the benefits of it. the look must be consistent throughout. additionally each service page should have some images related to the service

```html
<!DOCTYPE html>
<html lang="en">
<head>
<meta charset="utf-8">
<title>Clearline Water Services Ltd.</title>
<link rel="stylesheet" href="https://fonts.googleapis.com/css2?family=Arimo:wght@400;700&display=swap">
<style>
  :root {
    --page-bg: #e8e8e8;
    --nav-top: #676767;
    --nav-bottom: #3c3c3c;
    --white: #ffffff;
    --navy: #163659;
    --heading-dark: #0f2f57;
    --who-heading: #5b4d48;
    --body-dark: #2f3b46;
    --accent: #4fb3e6;
    --muted: #9a9a9a;
    --muted-light: #b0b0b0;
    --date: #6b6b6b;
    --footer-bg: #efefef;
    --social: #bdbdbd;
    --button-blue: #2f6ea6;
  }
  * { box-sizing: border-box; margin: 0; padding: 0; }
  html, body {
    width: 1200px; height: 1015px; overflow: hidden;
    background: var(--page-bg);
    font-family: "Arimo", Arial, sans-serif;
  }
  .page {
    position: relative; width: 1300px; height: 1100px;
    transform: scale(0.923077); transform-origin: 0 0;
  }
  .abs { position: absolute; }

  /* navigation */
  .site-nav {
    position: absolute; left: 0; top: 0; width: 1300px; height: 50px;
    background: linear-gradient(var(--nav-top), var(--nav-bottom));
  }
  .nav-link { position: absolute; top: 16px; color: var(--white); font-size: 15px; text-decoration: none; }
  .search-label { position: absolute; left: 910px; top: 16px; color: #a9a9a9; font-size: 15px; }
  .search-field {
    position: absolute; left: 968px; top: 10px; width: 221px; height: 27px;
    background: var(--white); border-radius: 3px;
  }
  .search-field svg { position: absolute; right: 4px; top: 3px; }

  /* hero and projects band */
  .hero-band {
    position: absolute; left: 100px; top: 50px; width: 1100px; height: 647px;
    background:
      radial-gradient(ellipse 380px 120px at 300px 120px, rgba(255,255,255,.55), transparent 70%),
      radial-gradient(ellipse 300px 90px at 700px 60px, rgba(255,255,255,.5), transparent 70%),
      radial-gradient(ellipse 260px 80px at 450px 230px, rgba(255,255,255,.35), transparent 70%),
      linear-gradient(#c4e8fb 0%, #7cc7f0 22%, #3a9edb 45%, #1f74b6 62%, #114a82 82%, #0a335f 100%);
  }
  .brand {
    position: absolute; left: 135px; top: 95px;
    color: var(--navy); font-weight: 700; font-size: 31px; line-height: 31px; letter-spacing: -0.5px;
  }
  .phone {
    position: absolute; left: 878px; top: 84px; color: var(--white); font-size: 32px;
    display: flex; align-items: center; gap: 4px;
  }
  .hero-photo {
    position: absolute; left: 740px; top: 165px; width: 425px; height: 180px;
    border: 5px solid var(--white); border-radius: 16px;
    background: radial-gradient(ellipse at 60% 60%, #dfeefa, #8fb8da 45%, #3f6f9b 80%, #2c5882);
  }
  .who-title { position: absolute; left: 140px; top: 213px; font-size: 34px; font-weight: 700; color: var(--who-heading); }
  .who-text { position: absolute; left: 144px; top: 258px; width: 530px; font-size: 15px; line-height: 18px; color: var(--body-dark); }
  .divider { position: absolute; left: 138px; top: 366px; width: 1020px; height: 1px; background: #1c4f84; }
  .section-title-dark { position: absolute; left: 140px; top: 392px; font-size: 20px; font-weight: 700; color: var(--heading-dark); }

  .project { position: absolute; top: 432px; width: 158px; }
  .project-photo { width: 156px; height: 104px; border: 4px solid var(--white); }
  .project-title { margin-top: 9px; color: var(--white); font-size: 14px; text-decoration: underline; }
  .project-text { margin-top: 9px; color: var(--white); font-size: 11px; line-height: 13px; text-align: justify; text-align-last: justify; }
  .btn-more {
    position: absolute; left: 1072px; top: 636px; width: 97px; height: 27px;
    background: var(--button-blue); border: 1px solid #7fb1db; border-radius: 3px;
    color: var(--white); font-size: 12px; line-height: 25px; text-align: center;
  }

  /* lower white section */
  .content-panel { position: absolute; left: 100px; top: 697px; width: 1100px; height: 318px; background: var(--white); }
  .section-title-light { position: absolute; font-size: 20px; font-weight: 700; color: var(--accent); }
  .news-frame { position: absolute; left: 129px; width: 173px; height: 103px; border: 1px solid #dcdcdc; padding: 4px; }
  .news-photo { width: 100%; height: 100%; }
  .news-body { position: absolute; left: 316px; width: 296px; }
  .news-title { font-size: 17px; color: var(--muted); text-decoration: underline; }
  .news-date { margin-top: 6px; font-size: 12px; color: var(--date); }
  .news-text { margin-top: 2px; font-size: 12px; line-height: 15px; color: var(--muted-light); }
  .btn-archive {
    position: absolute; left: 547px; top: 969px; width: 67px; height: 27px;
    background: #f6f6f6; border: 1px solid #dcdcdc; border-radius: 3px;
    color: var(--muted); font-size: 12px; line-height: 25px; text-align: center;
  }
  .service-photo { position: absolute; }

  /* footer */
  .site-footer { position: absolute; left: 100px; top: 1015px; width: 1100px; height: 65px; background: var(--footer-bg); }
  .copyright { position: absolute; left: 140px; top: 1041px; font-size: 13px; color: #8a8a8a; }
  .social-square { position: absolute; top: 1029px; width: 40px; height: 40px; background: var(--social); }
</style>
</head>
<body>
<div class="page">

  <nav class="site-nav">
    <a class="nav-link" style="left:120px;top:15px" href="#">Home page</a>
    <a class="nav-link" style="left:233px" href="#">About Us</a>
    <a class="nav-link" style="left:324px" href="#">Our Services</a>
    <a class="nav-link" style="left:440px" href="#">Latest News</a>
    <a class="nav-link" style="left:557px" href="#">Contact Us</a>
    <span class="search-label">Search</span>
    <div class="search-field">
      <svg width="20" height="20" viewBox="0 0 20 20" aria-hidden="true">
        <circle cx="12" cy="8" r="6" fill="none" stroke="#cfcfcf" stroke-width="2"/>
        <line x1="7.5" y1="12.5" x2="2" y2="18" stroke="#cfcfcf" stroke-width="2.5" stroke-linecap="round"/>
      </svg>
    </div>
  </nav>

  <div class="hero-band" role="img" aria-label="Blue sky with soft white clouds fading into deep water blue"></div>

  <div class="brand">CLEARLINE<br>WATER SERVICES LTD.</div>

  <div class="phone">
    <svg width="32" height="38" viewBox="0 0 32 38" aria-hidden="true">
      <path d="M9 3 C4 5 2 10 4 18 C6 26 12 33 19 36 C22 37 25 35 27 32 L22 26 C20 27 18 28 16 26 C13 22 11 18 11 14 C11 12 13 11 15 10 L12 3 Z" fill="#5fb6ec"/>
    </svg>
    <span>(800) - 555 0142</span>
  </div>

  <div class="hero-photo" role="img" aria-label="Splash of clear water against a pale blue background"></div>

  <h1 class="who-title">Who We Are?</h1>
  <p class="who-text">Sed elementum quis quam at elementum. Nullam vulputate risus sit amet imperdiet consequat. Morbi vestibulum aliquet magna ac semper. Cras vestibu-lum ante a eleifend mattis.</p>

  <div class="divider"></div>
  <h2 class="section-title-dark">OUR PROJECTS</h2>

  <article class="project" style="left:140px">
    <div class="project-photo" role="img" aria-label="Water poured from a jug into a glass" style="background:linear-gradient(135deg,#f4f8fa,#c9dbe3 55%,#eef3f5)"></div>
    <div class="project-title">Lorem ipsum dolor sit</div>
    <p class="project-text">Cras id dui eget odio scelerisque volutpat et id orci. Nulla sagittis, nulla non lobortis elementun</p>
  </article>
  <article class="project" style="left:360px">
    <div class="project-photo" role="img" aria-label="Open aeration tank at a treatment plant" style="background:linear-gradient(#c9d6df 0%,#8a9a8a 25%,#8c6a62 45%,#b7958c 100%)"></div>
    <div class="project-title">Lorem ipsum dolor sit</div>
    <p class="project-text">Cras id dui eget odio scelerisque volutpat et id orci. Nulla sagittis, nulla non lobortis elementun</p>
  </article>
  <article class="project" style="left:576px">
    <div class="project-photo" role="img" aria-label="Circular clarifier basin with walkway" style="background:linear-gradient(#7d8a62 0%,#3a6fa8 40%,#1e4a86 70%,#8d9a74 100%)"></div>
    <div class="project-title">Lorem ipsum dolor sit</div>
    <p class="project-text">Cras id dui eget odio scelerisque volutpat et id orci. Nulla sagittis, nulla non lobortis elementun</p>
  </article>
  <article class="project" style="left:794px;top:432px">
    <div class="project-photo" role="img" aria-label="Chrome tap with running water on blue" style="background:linear-gradient(135deg,#0a4fa6,#2a8ee0 50%,#6fc0f2)"></div>
    <div class="project-title" style="margin-top:8px">Lorem ipsum dolor sit</div>
    <p class="project-text" style="margin-top:7px">Cras id dui eget odio scelerisque volutpat et id orci. Nulla sagittis, nulla non lobortis elementun</p>
  </article>
  <article class="project" style="left:1002px">
    <div class="project-photo" role="img" aria-label="Water poured from a jug into a glass" style="background:linear-gradient(135deg,#f4f8fa,#c9dbe3 55%,#eef3f5)"></div>
    <div class="project-title" style="margin-top:8px">Lorem ipsum dolor sit</div>
    <p class="project-text">Cras id dui eget odio scelerisque volutpat et id orci. Nulla sagittis, nulla non lobortis elementun</p>
  </article>

  <div class="btn-more">More Projects</div>

  <section class="content-panel"></section>

  <h2 class="section-title-light" style="left:133px;top:712px">LATEST NEWS</h2>

  <div class="news-frame" style="top:745px">
    <div class="news-photo" role="img" aria-label="Water flowing over a weir at a treatment plant" style="background:linear-gradient(120deg,#6e7a80,#cfd6da 45%,#5d6a70 75%,#2f3a40)"></div>
  </div>
  <div class="news-body" style="top:745px">
    <div class="news-title">Consectetur adipiscing elit. Integer</div>
    <div class="news-date">[11.06.2014]</div>
    <p class="news-text">Cras id dui eget odio scelerisque volutpat et orci. Nulla sagittis, nulla non lobortis elementun Cras id dui eget odio scelerisque volutpat et id orci...</p>
  </div>

  <div class="news-frame" style="top:867px">
    <div class="news-photo" role="img" aria-label="Plastic water bottle lying on its side" style="background:linear-gradient(90deg,#d6e9f4,#9cc7e2 50%,#3c7fbf 80%,#e8f2f8)"></div>
  </div>
  <div class="news-body" style="top:866px">
    <div class="news-title">Nulla cras adipiscing odio. elementun</div>
    <div class="news-date">[11.06.2014]</div>
    <p class="news-text">Cras id eget odio scelerisque volutpat et id orci. Nulla sagittis, nulla lobortis elementun Cras id dui eget odio scelerisque volutpat et id orci...</p>
  </div>

  <div class="btn-archive">Archive</div>

  <h2 class="section-title-light" style="left:720px;top:714px">OUR SERVICES</h2>

  <div class="service-photo" role="img" aria-label="Aeration basin with pumps" style="left:723px;top:756px;width:125px;height:104px;background:linear-gradient(#7b8a6a 0%,#9aa8a8 30%,#dfe7ea 60%,#5f7f9a 100%)"></div>
  <div class="service-photo" role="img" aria-label="Water droplet splash on dark background" style="left:879px;top:756px;width:130px;height:104px;background:radial-gradient(circle at 50% 45%,#dfe9ef,#6f8a9c 35%,#1d2a33 75%)"></div>
  <div class="service-photo" role="img" aria-label="Metal walkway over a treatment tank" style="left:1038px;top:756px;width:129px;height:104px;background:linear-gradient(#f3f3f3 0%,#c9cdd0 45%,#7a8086 75%,#3b3e42 100%)"></div>
  <div class="service-photo" role="img" aria-label="Water running from a tap" style="left:723px;top:890px;width:125px;height:104px;background:linear-gradient(90deg,#1f2a36,#a9bccb 50%,#2b3a48)"></div>
  <div class="service-photo" role="img" aria-label="Concrete settling tanks at a treatment plant" style="left:879px;top:890px;width:130px;height:103px;background:linear-gradient(#c7d4dc 0%,#8e927a 30%,#cbbba6 60%,#a99b88 100%)"></div>
  <div class="service-photo" role="img" aria-label="Water spilling over an outfall weir" style="left:1038px;top:890px;width:129px;height:103px;background:linear-gradient(#2c3a44 0%,#5b6d78 40%,#c7d3da 55%,#24343e 100%)"></div>

  <footer class="site-footer"></footer>
  <p class="copyright">Copyrights ©2014 Clearline Water Services LTD. All rights Reserved</p>
  <div class="social-square" style="left:1012px" aria-label="Social link"></div>
  <div class="social-square" style="left:1057px" aria-label="Social link"></div>
  <div class="social-square" style="left:1102px" aria-label="Social link"></div>
  <div class="social-square" style="left:1147px" aria-label="Social link"></div>

</div>
</body>
</html>
```